Financial Consulting Company in need of technical diagram

Attached is a basic template to follow, however the following changes must be made:
- Get rid of reflection boxes at the bottom
-Delete anything in parentheses
-Change top box to read "Uncover Value Opportunities"
-Change bottom right box to read "Sales and Operations Planning"
-Change bottom left box to read "Financial Planning"

Additionally we would like to see something a little more creative and cohesive. One possibility is using "Cheveron" type arrows to show the "wheel" effect.

Please email mtorvek@halbrine.example if you have any questions!
Updates

Please see newly uploaded image for an example of how we would like it re-created.

Project Deadline Extended

Industry/Entity Type

Financial

Requirements
Must have
• I'm looking for something that keeps the "wheel" approach, but is not a direct re-creation of the example given. The boxes for example, dont' necessarily need to stay boxes. Feel free to play around with placement as well.
Nice to have
• Please see green wheel for example of how it can be re-created.

```html
<!DOCTYPE html>
<html lang="en">
<head>
<meta charset="utf-8">
<title>Value Cycle Diagram</title>
<link rel="stylesheet" href="https://fonts.googleapis.com/css2?family=Carlito:wght@700&display=swap">
<style>
  :root {
    --bg: #ffffff;
    --label: #ffffff;
    --red: #c0504d;
    --red-side: #9e3c39;
    --green: #9bbb59;
    --green-side: #7c9a42;
    --purple: #8064a2;
    --purple-side: #624b82;
    --teal: #4bacc6;
    --teal-side: #358ba3;
    --orange: #f79646;
    --orange-side: #d6782c;
  }
  html, body {
    margin: 0;
    padding: 0;
    overflow: hidden;
    background: var(--bg);
  }
  .canvas {
    width: 1200px;
    height: 900px;
    position: relative;
    overflow: hidden;
    background: var(--bg);
  }
  .cycle { display: block; }
  .stage-label {
    font-family: "Carlito", "Calibri", sans-serif;
    font-weight: 700;
    font-size: 29px;
    fill: var(--label);
    text-anchor: middle;
  }
  .bevel { fill: none; stroke: rgba(255,255,255,0.55); stroke-width: 2; }
  .connector { fill: none; stroke-width: 2; }
  .stage--red .face { fill: var(--red); }
  .stage--red .side { fill: var(--red-side); }
  .stage--green .face { fill: var(--green); }
  .stage--green .side { fill: var(--green-side); }
  .stage--purple .face { fill: var(--purple); }
  .stage--purple .side { fill: var(--purple-side); }
  .stage--teal .face { fill: var(--teal); }
  .stage--teal .side { fill: var(--teal-side); }
  .stage--orange .face { fill: var(--orange); }
  .stage--orange .side { fill: var(--orange-side); }
  .connector--red { stroke: var(--red); }
  .connector--green { stroke: var(--green); }
  .connector--purple { stroke: var(--purple); }
  .connector--teal { stroke: var(--teal); }
  .connector--orange { stroke: var(--orange); }
</style>
</head>
<body>
<main class="canvas">
  <svg class="cycle" width="1200" height="900" viewBox="0 0 1200 900" role="img" aria-label="Five-stage value cycle">
    <defs>
      <marker id="head-red" markerWidth="12" markerHeight="12" refX="10" refY="6" orient="auto" markerUnits="userSpaceOnUse"><path d="M1,1 L10,6 L1,11" fill="none" stroke="#c0504d" stroke-width="2"/></marker>
      <marker id="head-green" markerWidth="12" markerHeight="12" refX="10" refY="6" orient="auto" markerUnits="userSpaceOnUse"><path d="M1,1 L10,6 L1,11" fill="none" stroke="#9bbb59" stroke-width="2"/></marker>
      <marker id="head-purple" markerWidth="12" markerHeight="12" refX="10" refY="6" orient="auto" markerUnits="userSpaceOnUse"><path d="M1,1 L10,6 L1,11" fill="none" stroke="#8064a2" stroke-width="2"/></marker>
      <marker id="head-teal" markerWidth="12" markerHeight="12" refX="10" refY="6" orient="auto" markerUnits="userSpaceOnUse"><path d="M1,1 L10,6 L1,11" fill="none" stroke="#4bacc6" stroke-width="2"/></marker>
      <marker id="head-orange" markerWidth="12" markerHeight="12" refX="10" refY="6" orient="auto" markerUnits="userSpaceOnUse"><path d="M1,1 L10,6 L1,11" fill="none" stroke="#f79646" stroke-width="2"/></marker>
    </defs>

    <!-- Connectors -->
    <path class="connector connector--red" d="M725,268 L765,318" marker-end="url(#head-red)"/>
    <path class="connector connector--green" d="M818,498 Q826,548 792,590" marker-end="url(#head-green)"/>
    <path class="connector connector--purple" d="M602,690 L560,702" marker-end="url(#head-purple)"/>
    <path class="connector connector--teal" d="M362,532 Q328,478 346,422" marker-end="url(#head-teal)"/>
    <path class="connector connector--orange" d="M398,252 L440,222" marker-end="url(#head-orange)"/>

    <!-- Stage: Uncover Value Opportunities -->
    <g class="stage stage--red">
      <rect class="side" x="478" y="112" width="250" height="124" rx="16"/>
      <polygon class="side" points="462,130 490,112 728,128 728,220 700,250 700,130"/>
      <rect class="face" x="450" y="130" width="250" height="124" rx="16"/>
      <path class="bevel" d="M704,136 L724,122"/>
      <text class="stage-label" x="575" y="186">Uncover Value</text>
      <text class="stage-label" x="575" y="222">Opportunities</text>
    </g>

    <!-- Stage: Strategize and Align -->
    <g class="stage stage--green">
      <rect class="side" x="718" y="314" width="230" height="130" rx="16"/>
      <polygon class="side" points="702,332 730,314 948,330 948,428 920,460 920,332"/>
      <rect class="face" x="690" y="332" width="230" height="130" rx="16"/>
      <path class="bevel" d="M924,338 L944,324"/>
      <text class="stage-label" x="805" y="392">Strategize</text>
      <text class="stage-label" x="805" y="430">and Align</text>
    </g>

    <!-- Stage: Sales and Operations Planning -->
    <g class="stage stage--purple">
      <rect class="side" x="628" y="582" width="236" height="150" rx="16"/>
      <polygon class="side" points="612,600 640,582 864,598 864,716 836,748 836,600"/>
      <rect class="face" x="600" y="600" width="236" height="150" rx="16"/>
      <path class="bevel" d="M840,606 L860,592"/>
      <text class="stage-label" x="718" y="648">Sales and</text>
      <text class="stage-label" x="718" y="684">Operations</text>
      <text class="stage-label" x="718" y="720">Planning</text>
    </g>

    <!-- Stage: Financial Planning -->
    <g class="stage stage--teal">
      <rect class="side" x="352" y="552" width="236" height="130" rx="16"/>
      <polygon class="side" points="336,570 364,552 588,568 588,666 560,698 560,570"/>
      <rect class="face" x="324" y="570" width="236" height="130" rx="16"/>
      <path class="bevel" d="M564,576 L584,562"/>
      <text class="stage-label" x="442" y="626">Financial</text>
      <text class="stage-label" x="442" y="664">Planning</text>
    </g>

    <!-- Stage: Assess the Results -->
    <g class="stage stage--orange">
      <rect class="side" x="268" y="262" width="230" height="130" rx="16"/>
      <polygon class="side" points="252,280 280,262 498,278 498,376 470,408 470,280"/>
      <rect class="face" x="240" y="280" width="230" height="130" rx="16"/>
      <path class="bevel" d="M474,286 L494,272"/>
      <text class="stage-label" x="355" y="320">Assess the</text>
      <text class="stage-label" x="355" y="378">Results</text>
    </g>
  </svg>
</main>
</body>
</html>
```